Single Page Corporate Profile Web-site Design

We're a new IT Resourcing company called vanq5, and we need a ew single page corporate web-site to establish our credentials.

Our model is to extend IT resourcing to offer access to global resources, end to end management, and a structured approach resourcing process.

Phase 2 (out of scope) will be a full site build in approximately a month's time.

This project is to:
- Establish a look and feel for web, consistent with existing design work (logo an corporate presentation)
- Build the web pages
- Upload onto our domain hosting site (4&4)

The web-site:
We want a modern, clean and bold design.

We'd like a design that is consistent with our corporate presentation (sourceless supplied). In terms of look and feel and use of graphics.

KEY FEATURES
- Single page design.
- Navigation bar (to page sections) at the top of the page.
- No cookies (phase 1 design)
- Good example of preferred web page design:
www.plomtak42.com
https://brivo.com/regulator/days-with-brivo-regulator/
http://www.ombrelfinsystems.com
- Clear sections on page as structured in the attached slides.
- We would like some of the page sections to use imagery of your choice - but please no cliched "IT people" or "data-centre" images.
- Image use must be royalty free.

ANY ADVICE WELCOME ! It's been a while since we've done this.

Target Market(s)

Companies - mid-size, technically sophisticated IT developers.
Potential employees

Industry/Entity Type

It Company

Number of Pages Required

1 page

Font styles to use
Other font styles liked:
• calibri

Requirements
Must have
• Do's
• - Please use graphics and "look and feel" provided
• - Follow similar style of those sites provided
• - Take the provided content and develop it for the web
• - Page must load quickly (if you think there's too much on the page - say so, and we'll put it across a few"
• - Please use background imagery for some of the sections
Should not have
• Don'ts
• - Please don't use cliched imagery e.g. "IT people" or "data-centre lights"
• - Use dark colours

```html
<!DOCTYPE html>
<html lang="en">
<head>
<meta charset="utf-8">
<title>vanq5 – IT resourcing</title>
<link rel="stylesheet" href="https://fonts.googleapis.com/css2?family=Archivo+Black&family=Source+Sans+3:wght@400;600;700&family=Jost:wght@500&family=Carlito&display=swap">
<style>
  :root {
    --sky: #3aa8e8;
    --brand-blue: #1b8fd8;
    --cyan: #1aa3dc;
    --orange: #f7901e;
    --orange-deep: #f57f17;
    --ink: #222;
    --nav-ink: #444;
    --page: #f7f5f2;
    --panel: #fbfaf8;
    --footer: #4a4f5c;
    --footer-field: #5d6270;
    --bottom: #00aeef;
    --white: #fff;
  }
  * { box-sizing: border-box; margin: 0; padding: 0; }
  html, body { width: 865px; height: 1200px; overflow: hidden; }
  body { position: relative; background: var(--page); font-family: "Source Sans 3", sans-serif; color: var(--ink); }
  .abs { position: absolute; }

  .top-strip { left: 0; top: 0; width: 865px; height: 10px; background: var(--sky); }
  .site-header { left: 0; top: 10px; width: 865px; height: 62px; background: var(--white); }
  .brand { left: 98px; top: 2px; line-height: 1; }
  .brand-name { font: 700 40px/1 "Source Sans 3", sans-serif; color: var(--brand-blue); letter-spacing: -1px; }
  .brand-tag { font: 600 12px/1 "Source Sans 3", sans-serif; color: var(--brand-blue); margin-top: 1px; }
  .main-nav a { position: absolute; top: 34px; font-size: 16px; color: var(--nav-ink); text-decoration: none; }
  .main-nav a.current { border-bottom: 2px solid var(--orange); padding-bottom: 1px; }

  .hero { left: 0; top: 72px; width: 865px; height: 225px;
    background: linear-gradient(100deg, #5aa4d6 0%, #2d6fb6 35%, #24589e 60%, #3b74b8 80%, #7aa6cf 100%); }
  .hero-title { top: 27px; width: 865px; text-align: center; font: 28px/1 "Archivo Black", sans-serif; color: var(--white); letter-spacing: 0.5px; }
  .hero-title span { color: var(--orange); }
  .slide-arrow { top: 96px; width: 35px; height: 35px; background: var(--orange); }
  .promise { top: 84px; width: 200px; text-align: center; }
  .promise svg { display: block; margin: 0 auto; }
  .promise p { margin-top: 10px; font: 17px/18px "Archivo Black", sans-serif; color: var(--white); text-transform: uppercase; }

  .content-panel { left: 142px; top: 297px; width: 598px; height: 678px; background: var(--panel); }
  .band { left: 0; width: 865px; height: 45px; text-align: center; font: 18px/45px "Archivo Black", sans-serif; color: var(--white); }
  .band-orange { top: 328px; background: linear-gradient(90deg, #fde3c4 0%, #f9a44a 20%, var(--orange-deep) 50%, #f9a44a 80%, #fde3c4 100%); }
  .band-blue { top: 658px; background: linear-gradient(90deg, #a9dcf2 0%, #5cc0ea 25%, #3ab4e6 50%, #5cc0ea 75%, #bfe6f5 100%); }

  .timeline { left: 218px; top: 454px; width: 440px; height: 4px; background: var(--orange); }
  .pillar { top: 425px; width: 200px; text-align: center; }
  .pillar svg { display: block; margin: 0 auto; }
  .pillar h3 { margin-top: 6px; font: 500 23px/21px "Jost", sans-serif; color: var(--cyan); text-transform: uppercase; }
  .pillar p { margin-top: 9px; font: 700 12.5px/13.5px Arial, sans-serif; color: var(--cyan); }

  .focus-mark { left: 155px; top: 712px; width: 125px; text-align: center; }
  .focus-mark h3 { margin-top: 4px; font: 18px/1 "Archivo Black", sans-serif; color: var(--orange); }
  .focus-list { left: 310px; top: 726px; width: 420px; list-style: none; font: 16px/20px "Carlito", sans-serif; color: var(--orange); }
  .focus-list li { position: absolute; left: 0; width: 420px; }

  .site-footer { left: 0; top: 975px; width: 865px; height: 168px; background: var(--footer); color: var(--white); }
  .site-footer h4 { position: absolute; top: 8px; font: 400 20px/1 "Source Sans 3", sans-serif; }
  .site-footer p { position: absolute; font-size: 11px; line-height: 16.3px; }
  .social { left: 553px; top: 43px; display: flex; gap: 13px; }
  .social span { width: 12px; height: 12px; border-radius: 50%; background: var(--white); }
  .search { left: 552px; top: 70px; width: 183px; height: 30px; background: var(--footer-field); border: 1px solid #8b909c; }
  .search-btn { left: 735px; top: 70px; width: 32px; height: 30px; background: var(--orange); }

  .bottom-bar { left: 0; top: 1143px; width: 865px; height: 57px; background: var(--bottom); }
  .bottom-bar .brand { left: 690px; top: 6px; }
  .bottom-bar .brand-name { font-size: 34px; color: var(--orange); }
  .bottom-bar .brand-tag { font-size: 10px; color: var(--brand-blue); }
</style>
</head>
<body>
  <div class="abs top-strip"></div>

  <header class="abs site-header">
    <div class="abs brand">
      <div class="brand-name">vanq5</div>
      <div class="brand-tag">IT resourcing</div>
    </div>
    <nav class="main-nav">
      <a class="current" style="left:232px">Home</a>
      <a style="left:294px">About Us</a>
      <a style="left:375px">Services</a>
      <a style="left:448px">Our DNA</a>
      <a style="left:523px">Competencies</a>
      <a style="left:639px">Delivery</a>
      <a style="left:714px">Contact</a>
    </nav>
  </header>

  <section class="abs hero" role="img" aria-label="Close-up of a blue keyboard beside glowing fibre-optic strands">
    <h1 class="abs hero-title">WE WANTED TO DO SOMETHING <span>DIFFERENT</span></h1>
    <div class="abs slide-arrow" style="left:0">
      <svg width="35" height="35"><path d="M20 11 L13 17.5 L20 24" fill="none" stroke="#fff" stroke-width="3"/></svg>
    </div>
    <div class="abs slide-arrow" style="left:831px">
      <svg width="35" height="35"><path d="M15 11 L22 17.5 L15 24" fill="none" stroke="#fff" stroke-width="3"/></svg>
    </div>

    <div class="abs promise" style="left:118px">
      <svg width="74" height="74"><circle cx="37" cy="37" r="35" fill="#1fa0e0"/><circle cx="37" cy="37" r="28" fill="#fff"/>
        <text x="37" y="46" text-anchor="middle" font-family="Archivo Black, sans-serif" font-size="24" fill="#111">$</text></svg>
      <p>Charge less,<br>for doing more</p>
    </div>
    <div class="abs promise" style="left:332px">
      <svg width="74" height="74"><circle cx="37" cy="37" r="35" fill="#1fa0e0"/><circle cx="37" cy="37" r="28" fill="#fff"/>
        <path d="M24 36 h7 v15 h-7z M33 36 l6-11 c3 0 4 2 3 6 l-1 3 h8 c2 0 3 2 2 4 l-2 10 c-1 2-2 3-4 3 h-12z" fill="#111"/></svg>
      <p>Always<br>deliver</p>
    </div>
    <div class="abs promise" style="left:557px">
      <svg width="74" height="74"><circle cx="37" cy="37" r="35" fill="#1fa0e0"/><circle cx="37" cy="37" r="28" fill="#fff"/>
        <path d="M20 37 Q37 22 54 37 Q37 52 20 37z" fill="#111"/><circle cx="37" cy="37" r="6" fill="#fff"/><circle cx="37" cy="37" r="3" fill="#111"/></svg>
      <p>Bring some<br>rigour</p>
    </div>
  </section>

  <div class="abs content-panel"></div>

  <h2 class="abs band band-orange">AN ITERATION OF TRADITIONAL RESOURCING</h2>

  <div class="abs timeline"></div>
  <div class="abs pillar" style="left:118px">
    <svg width="60" height="60"><circle cx="30" cy="30" r="28" fill="#1fa8e6" stroke="#111" stroke-width="3"/>
      <path d="M28 14 V31 L40 43" fill="none" stroke="#111" stroke-width="3"/></svg>
    <h3>Time<br>to hire</h3>
    <p>Combine local<br>market coverage,<br>with access to global<br>markets to deliver<br>exceptional people<br>quickly.</p>
  </div>
  <div class="abs pillar" style="left:335px">
    <svg width="60" height="60"><circle cx="30" cy="30" r="28" fill="#1fa8e6" stroke="#111" stroke-width="3"/>
      <text x="30" y="42" text-anchor="middle" font-family="Jost, sans-serif" font-size="34" fill="#111">$</text></svg>
    <h3>Cost<br>to hire</h3>
    <p>Reduce cost per hire<br>by sharing the<br>financial benefits of<br>resourcing more<br>efficiently together.</p>
  </div>
  <div class="abs pillar" style="left:558px">
    <svg width="60" height="60"><circle cx="30" cy="30" r="28" fill="#1fa8e6" stroke="#111" stroke-width="3"/>
      <path d="M23 13 h14 v10 h-14z" fill="#111"/><circle cx="30" cy="34" r="10" fill="#111"/><circle cx="30" cy="34" r="4" fill="#1fa8e6"/></svg>
    <h3>Quality<br>of hires</h3>
    <p>Bring IT service<br>delivery quality to<br>the resourcing<br>process to assure the<br>quality of hires.</p>
  </div>

  <h2 class="abs band band-blue">WE ARE FOCUSED ON CUSTOMER WHO HAVE:</h2>

  <div class="abs focus-mark">
    <svg width="125" height="120" viewBox="0 0 125 120">
      <circle cx="55" cy="68" r="50" fill="#1fa8e6"/><circle cx="55" cy="68" r="40" fill="#fff"/>
      <circle cx="55" cy="68" r="30" fill="#1fa8e6"/><circle cx="55" cy="68" r="20" fill="#fff"/>
      <circle cx="55" cy="68" r="10" fill="#1fa8e6"/>
      <path d="M55 68 L108 15" stroke="#fff" stroke-width="8"/>
      <path d="M55 68 L108 15" stroke="#1fa8e6" stroke-width="4"/>
      <path d="M100 12 L114 2 L122 10 L112 24z" fill="#1fa8e6"/>
    </svg>
    <h3>OUR FOCUS</h3>
  </div>
  <ul class="abs focus-list">
    <li style="top:0">. High reliance on IT</li>
    <li style="top:36px">. Significant application development requirement</li>
    <li style="top:77px">. Early or mid-growth phases ( up to 250 employees )</li>
    <li style="top:114px">. Resourcing is a critical hindrance to growth</li>
    <li style="top:148px">. Limited recruitment capability and &nbsp;immature recruitment processes</li>
  </ul>

  <footer class="abs site-footer">
    <h4 style="left:158px">About us:</h4>
    <p style="left:157px;top:36px;width:150px">We created vanq5 because we wanted to offer something different in IT resourcing. We’re expert at what we do, with a track record of IT Service Delivery and Resourcing excellence in high growth environments:</p>
    <h4 style="left:385px">Contact:</h4>
    <p style="left:391px;top:38px">Larkspur Row 3<br>United States<br>11 4820 553716</p>
    <h4 style="left:553px">Connect:</h4>
    <div class="abs social" aria-label="Social links">
      <span></span><span></span><span></span><span></span><span></span><span></span><span></span><span></span><span></span>
    </div>
    <div class="abs search"></div>
    <div class="abs search-btn">
      <svg width="32" height="30"><circle cx="18" cy="12" r="6" fill="none" stroke="#fff" stroke-width="2"/><path d="M14 16 L8 22" stroke="#fff" stroke-width="2.5"/></svg>
    </div>
  </footer>

  <div class="abs bottom-bar">
    <div class="abs brand">
      <div class="brand-name">vanq5</div>
      <div class="brand-tag">IT resourcing</div>
    </div>
  </div>
</body>
</html>
```